deceased estate clean ups brochures

we would like a brochure to reresent our business we already have new web site and want to do DL A4 brochure to give out to promote our business we already have logo www.brightvale.com.au is where you can get all info needed

Target Market(s)

families with loved ones that have past away
people done sizing or needing to decluter

Colors
cadf82
33b8a4
886aae
33a6d7

```html
<!DOCTYPE html>
<html lang="en">
<head>
<meta charset="utf-8">
<title>Brightvale Deceased Estate Clean Ups – DL Brochure</title>
<link href="https://fonts.googleapis.com/css2?family=Cinzel:wght@400;700&family=Open+Sans:wght@400;600;700&family=Tinos:wght@400;700&display=swap" rel="stylesheet">
<style>
:root{
  --board:#a87b52;
  --lime:#b5d44a;
  --lime-soft:#cadf82;
  --green:#2aa24a;
  --green-text:#2e9e48;
  --purple:#886aae;
  --sky:#cfe9f4;
  --paper:#f4f6f8;
  --ink:#111111;
  --body:#3a3a3a;
  --white:#ffffff;
}
*{margin:0;padding:0;box-sizing:border-box}
html,body{width:898px;height:1200px;overflow:hidden}
body{background:var(--board);position:relative;font-family:"Open Sans",sans-serif;color:var(--body)}
.side-label{position:absolute;left:0;width:898px;text-align:center;font-family:"Tinos",serif;font-weight:700;font-size:22px;color:var(--white)}
.side-label.top{top:82px}
.side-label.bottom{top:1116px}
.sheet{position:absolute;left:115px;width:673px;height:476px;box-shadow:2px 3px 5px rgba(0,0,0,.35);overflow:hidden}
.sheet.outer{top:122px}
.sheet.inner{top:624px;background:var(--paper)}
.panel{position:absolute;top:0;height:476px;width:224px}
.panel.process{left:0;background:var(--lime);color:var(--ink);padding:0 18px 0 21px}
.panel.cover-inside{left:224px;width:225px;background:var(--paper);text-align:center}
.panel.front{left:449px;background:var(--sky);text-align:center}

.process h2{font-family:"Cinzel",serif;font-weight:400;font-size:15px;margin-top:26px;color:var(--ink)}
.step{margin-top:11px}
.step h3{font-size:10px;font-weight:700;color:var(--white);letter-spacing:.3px}
.step p{font-size:7.6px;line-height:9.6px;text-align:justify;margin-top:2px}
.step ul{list-style:none;margin-top:2px}
.step li{font-size:7.6px;line-height:9.6px;position:relative;padding-left:12px;margin-bottom:2px;text-align:justify}
.step li::before{content:"";position:absolute;left:0;top:2px;width:7px;height:7px;border-radius:50%;background:var(--white)}
.staff-box{position:absolute;left:18px;top:344px;width:192px;height:110px;background:var(--purple);border-radius:4px;color:var(--white);text-align:center;padding:8px 8px;box-shadow:0 6px 6px -3px rgba(0,0,0,.3)}
.staff-box h4{font-size:11px;font-weight:600;line-height:14px}
.staff-box p{font-size:6.2px;line-height:8.6px;margin-top:6px}

.cover-inside h1{font-family:"Cinzel",serif;color:var(--green-text);font-size:18.5px;line-height:22px;font-weight:700;margin-top:24px}
.service-list{margin:4px 23px 0}
.service-list li{list-style:none;font-family:"Cinzel",serif;font-size:11.5px;line-height:14px;color:var(--ink);padding:3px 0 4px;border-bottom:1px solid var(--lime)}
.service-list li:last-child{border-bottom:none}
.photo-frame{position:absolute;left:9px;top:159px;width:206px;height:119px;border:2px solid var(--purple);border-radius:4px;background:linear-gradient(135deg,#e9e4dc,#c9b8a2 55%,#8c7a66);box-shadow:0 6px 6px -4px rgba(0,0,0,.35)}
.cover-contact{position:absolute;left:0;top:296px;width:225px;text-align:center}

.brand{font-family:"Cinzel",serif;font-weight:700;color:var(--ink);letter-spacing:1px}
.brand-mark{display:inline-block;border-radius:50%;background:var(--green)}
.cover-contact .brand-mark{width:44px;height:44px}
.cover-contact .brand{font-size:22px;line-height:26px;margin-top:22px}
.phone{font-family:"Tinos",serif}
.cover-contact .phone{color:var(--green-text);font-size:23px;line-height:26px;margin-top:8px}
.address{font-family:"Tinos",serif;font-size:11px;line-height:14px;color:var(--ink);margin-top:2px}
.email-spaced{font-family:"Tinos",serif;font-size:9px;line-height:12px;letter-spacing:1.2px;color:var(--ink);margin-top:2px}

.front .eyebrow{font-family:"Cinzel",serif;font-size:21px;color:var(--ink);margin-top:26px;letter-spacing:.5px}
.front .brand-mark{width:52px;height:52px;margin-top:20px}
.front .brand{font-size:27px;margin-top:12px}
.scene-art{position:absolute;left:0;top:190px;width:224px;height:186px;border-radius:0 0 112px 112px;background:linear-gradient(180deg,#bfe2f0 0%,#f3d7a6 45%,#c65c4a 65%,#6fb24c 100%)}
.front-base{position:absolute;left:0;top:360px;width:224px;height:116px;background:var(--green)}
.front-contact{position:absolute;left:0;top:370px;width:224px;color:var(--white)}
.front-contact .phone{font-size:27px}
.front-contact .email{font-family:"Tinos",serif;font-size:11.5px;margin-top:4px}
.front-contact .web{font-family:"Tinos",serif;font-weight:700;font-size:15px;margin-top:2px}

.top-band{position:absolute;left:0;top:0;width:673px;height:9px;background:linear-gradient(90deg,var(--green),var(--lime-soft),var(--green))}
.bottom-band{position:absolute;left:0;top:460px;width:673px;height:16px;background:linear-gradient(90deg,var(--green),var(--lime-soft),var(--green))}
.col{position:absolute;top:0;width:224px;height:310px;padding:22px 19px 0 21px}
.col.clearing{left:0}
.col.sale{left:224px;width:225px;padding-top:24px}
.col.repairs{left:449px}
.col h2{font-family:"Cinzel",serif;font-weight:400;color:var(--green-text);font-size:15px;line-height:16.5px}
.col p{font-size:7.6px;line-height:9.6px;text-align:justify;margin-top:8px}
.col h4{font-size:9.5px;font-weight:600;color:var(--purple);margin-top:10px}
.dots{list-style:none;margin-top:6px}
.dots li{font-size:7.6px;line-height:12.3px;padding-left:11px;position:relative}
.dots li::before{content:"";position:absolute;left:0;top:3.5px;width:6px;height:6px;border-radius:50%;background:var(--purple)}
.dots small{font-size:6px}
.col p.junk{font-size:7.6px;line-height:11px;margin-top:10px;text-align:left}
.junk b{font-weight:400;color:var(--purple);font-size:9px}
.query-box{position:absolute;left:18px;top:237px;width:181px;height:60px;background:var(--lime);border-radius:3px;text-align:center;color:var(--ink);padding-top:5px;box-shadow:0 6px 6px -3px rgba(0,0,0,.3)}
.query-box .lead{font-size:8.6px;font-weight:600}
.query-box .phone{font-size:22px;line-height:24px}
.query-box .email{font-family:"Tinos",serif;font-size:8.6px}
.photo{position:absolute;top:310px;height:150px}
.photo.cluttered-room{left:0;width:224px;background:linear-gradient(135deg,#5a4a3a,#a99882 50%,#3e3a36)}
.photo.renovation-room{left:224px;width:225px;background:linear-gradient(180deg,#d9d4c8,#9e978a 60%,#6f675c)}
.photo.house-exterior{left:449px;width:224px;background:linear-gradient(135deg,#f5d48a,#c8a27a 40%,#e8e4dc 70%,#8a6a4a)}
</style>
</head>
<body>
<div class="side-label top">Side 1</div>

<section class="sheet outer">
  <div class="panel process">
    <h2>OUR 5 STEP PROCESS</h2>
    <div class="step">
      <h3>STEP 1:</h3>
      <p>We start with a consultation at the property, understanding our client’s needs, requests and priorities. Create a plan of what needs to be done in each step of your move. Provide a personalized quote.</p>
    </div>
    <div class="step">
      <h3>STEP 2:</h3>
      <p>Pre-sale decluttering and sorting of items. Unwanted items to be sold, given to friends, family or charity.</p>
    </div>
    <div class="step">
      <h3>STEP 3:</h3>
      <ul>
        <li>We thoroughly clear and clean the property (inside and outside) prior to sale or rent.</li>
        <li>House to be staged and set up to enhance its presentation for sale or rent.</li>
        <li>Rubbish to be picked up.</li>
        <li>Garden to be tidied.</li>
        <li>After settlement, we begin to pack your possessions ready to be moved as directed.</li>
      </ul>
    </div>
    <div class="step">
      <h3>STEP 4:</h3>
      <p>Organising and arranging transport of your possessions.</p>
    </div>
    <div class="staff-box">
      <h4>Our experienced staff can provide comprehensive services:</h4>
      <p>Bereavement house clearances carried out in a sensitive manner. Management of your property. If you are not local to the area or unable to visit the property.</p>
      <p>Photographic updates throughout the service and at completion. Clearance and cleaning services are available. Fully trained professional staff.</p>
    </div>
  </div>

  <div class="panel cover-inside">
    <h1>DECEASED ESTATE<br>CLEAN UPS</h1>
    <ul class="service-list">
      <li>House Clearing</li>
      <li>Preparation for Sale</li>
      <li>Cosmetic Repairs and House Maintenance</li>
    </ul>
    <div class="photo-frame" role="img" aria-label="Photo of cleaners wiping a table and mopping a wooden floor"></div>
    <div class="cover-contact">
      <span class="brand-mark"></span>
      <div class="brand">BRIGHTVALE</div>
      <div class="phone">0400 318 642</div>
      <div class="address">PO Box 208, Elmwood 3100</div>
      <div class="email-spaced">info@brightvalemelbourne.com.au</div>
    </div>
  </div>

  <div class="panel front">
    <div class="eyebrow">DECEASED ESTATE</div>
    <span class="brand-mark"></span>
    <div class="brand">BRIGHTVALE</div>
    <div class="scene-art" role="img" aria-label="Illustration of a house with belongings being loaded into a skip truck"></div>
    <div class="front-base"></div>
    <div class="front-contact">
      <div class="phone">0400 318 642</div>
      <div class="email">info@brightvalemelbourne.com.au</div>
      <div class="web">www.brightvale.com.au</div>
    </div>
  </div>
</section>

<section class="sheet inner">
  <div class="top-band"></div>

  <div class="col clearing">
    <h2>HOUSE CLEARING</h2>
    <p>We can work with family or trustees in providing services to prepare the property for rental or sale.</p>
    <p>Following the loss of a family member, many people will find the thought of dealing with the clearance of personal effects and property in a deceased estate a daunting one.</p>
    <p>We understand the difficulties with making arrangements at this time and offer a tailored service to assist with your personal situation.</p>
    <h4>We provide:</h4>
    <ul class="dots">
      <li>Cleaning of walls, floors, and ceilings</li>
      <li>Window cleaning</li>
      <li>Bathrooms, kitchens and living spaces</li>
      <li>Packing of delicate and personal items</li>
      <li>Steam cleaning</li>
      <li>Shed and garage cleaning</li>
      <li>Rubbish removal</li>
      <li>Gardening/ Landscaping</li>
      <li>All maintenance repairs</li>
      <li>Interior decorating</li>
    </ul>
  </div>

  <div class="col sale">
    <h2>PREPARATION FOR SALE</h2>
    <p>Tidying up before selling your house? In need of an estate clean up? Doing renovations or construction, or are in need of an alternative to skips we can help.</p>
    <p>We take almost anything that is non-hazardous that two people can lift: old unwanted furniture and appliances, garden waste, house and renovation debris, excess packaging and cardboard, office furniture and equipment, electronics and TVs – we take it all, whether you have a lot or a little.</p>
    <p>We make sure it gets disposed of properly through donation or recycling. The dump is always our last resort.</p>
    <p class="junk"><b>Household Junk Removal:</b> Appliance, Refrigerator, Mattress, Furniture, Carpet TV, Tyre &amp; Scrap Metal</p>
    <p class="junk"><b>Office Junk Removal:</b> Computer Recycling, Printer Recycling, Monitor Recycling</p>
    <p class="junk"><b>General Junk Removal:</b> Green Waste, Rubbish, Garbage Removal Alternative, Skip Bin Alternative, Junk, Construction Cleanout &amp; Estate Cleanout</p>
  </div>

  <div class="col repairs">
    <h2>COSMETIC REPAIRS AND HOUSE MAINTENANCE</h2>
    <p>At Brightvale, we are experienced in cosmetic house repairs and renovations.</p>
    <h4>Common additional services requested by our customers include:</h4>
    <ul class="dots">
      <li>Plastering</li>
      <li>Painting</li>
      <li>New carpets or floorboards</li>
      <li>Electrical &amp; Plumbing <small>(by Licensed Tradespeople)</small></li>
      <li>Bathroom and kitchen renovations</li>
      <li>Garden maintenance and landscaping</li>
      <li>Fencing</li>
      <li>Brickwork</li>
      <li>Decking</li>
    </ul>
    <div class="query-box">
      <div class="lead">If you have any queries, Please call</div>
      <div class="phone">0400 318 642</div>
      <div class="email">info@brightvalemelbourne.com.au</div>
    </div>
  </div>

  <div class="photo cluttered-room" role="img" aria-label="Photo of a cluttered bedroom filled with clothes and belongings"></div>
  <div class="photo renovation-room" role="img" aria-label="Photo of an empty room under renovation with a ladder"></div>
  <div class="photo house-exterior" role="img" aria-label="Photo of a two-storey house exterior with scaffolding and paint tins"></div>
  <div class="bottom-band"></div>
</section>

<div class="side-label bottom">Side 1</div>
</body>
</html>
```